Need posters that inspire entrepreneurs

I want to create beautiful, inspiring wall art. I'm looking for a designer to create an awesome sample (note this sample is not for real use). The winning design will form the foundation of our art "style" so there will be LOTS of ongoing work for the winning designer.

It's your challenge to create a style that is clean, inspiring and timeless, and possibly can be adapted to different colour palettes.

Looking for a perfect execution of words, image and design.

The attached example shows one idea. It should serve as an idea only.

Format of the images should be either rectangular or square. Exact size is preferably UK A4 (US letter) or max A3. Assume that a display would consist of a 4 x 4 image grid so size needs to allow for that in a small to medium size office.

The quotes I want in the 3 samples (each in an individual poster - not combined in 1 poster). Each quote should have it's own, the reason for three is to prove the design work on more than one quote. The quotes are:

1) Failure is the condiment that gives success its flavor.
– Dorian Welsby

2) Whether you think you can or think you can’t, you’re right.
– Oswald Pike

3) Ever tried. Ever failed. No matter. Try Again. Fail again. Fail better.
– Lionel Marwick

Each design should include the image of the person and the quote + any design elements you consider relevant. You should find relevant images of the individuals being quoted. The final images will not be published or used commercially in any way.

Font styles to use
Serif
Sans Serif

Colors

Designer to choose colors to be used in the design.

Requirements
Must have
• Words and headshot image - 1 per poster design.
• Please consider in the design that there will not always be photographs of the person quoted and as such the design will need to hold, whether the source is a photo, sketch or something else.
Nice to have
• None, but note that the final image will be printed on a wall mounted board, printed to the edge but not on the edge. The board will have black or white edges so consider in the design.
Should not have
• None

```html
<!DOCTYPE html>
<html lang="en">
<head>
<meta charset="utf-8">
<title>Fail Better – Lionel Marwick</title>
<link rel="stylesheet" href="https://fonts.googleapis.com/css2?family=Bodoni+Moda:opsz,wght@6..96,700;6..96,800&display=swap">
<style>
  :root {
    --bg-brown: #43281a;
    --portrait-light: #b5977a;
    --portrait-mid: #7a5a40;
    --portrait-shadow: rgba(122, 90, 64, 0.55);
    --bg-clear: rgba(67, 40, 26, 0);
    --text-cream: #fffaf2;
  }
  html, body {
    margin: 0;
    padding: 0;
    overflow: hidden;
    background: var(--bg-brown);
  }
  .poster {
    position: relative;
    width: 1200px;
    height: 1200px;
    overflow: hidden;
    background: var(--bg-brown);
    font-family: "Bodoni Moda", "Didot", serif;
    color: var(--text-cream);
  }
  .portrait {
    position: absolute;
    left: 520px;
    top: 420px;
    width: 680px;
    height: 780px;
    background:
      radial-gradient(ellipse 36% 38% at 56% 48%, var(--portrait-light) 0%, var(--portrait-mid) 55%, var(--bg-clear) 100%),
      radial-gradient(ellipse 34% 22% at 62% 100%, var(--portrait-shadow) 0%, var(--bg-clear) 100%);
  }
  .quote {
    position: absolute;
    left: 80px;
    top: 278px;
    margin: 0;
    font-size: 76px;
    font-weight: 700;
    line-height: 93px;
    letter-spacing: -1.5px;
  }
  .quote-line {
    display: block;
    white-space: nowrap;
  }
  .attribution {
    position: absolute;
    left: 80px;
    top: 886px;
    margin: 0;
    font-size: 27px;
    font-weight: 700;
    letter-spacing: 0;
  }
</style>
</head>
<body>
  <main class="poster">
    <div class="portrait" role="img" aria-label="Sepia headshot portrait of Lionel Marwick wearing round glasses pushed up on his forehead"></div>
    <blockquote class="quote">
      <span class="quote-line">Ever tried.</span>
      <span class="quote-line">Ever failed.</span>
      <span class="quote-line">No matter.</span>
      <span class="quote-line">Try Again.</span>
      <span class="quote-line">Fail again.</span>
      <span class="quote-line">Fail better.</span>
    </blockquote>
    <p class="attribution">– Lionel Marwick</p>
  </main>
</body>
</html>
```